Postcard Design

We are a home remodeling company we do a complete home remodeling Including bathrooms ,kitchen ,basement ,interior exterior work .
We doing hardwood floors ,painting ,ceramic tile, baseboards ,casings ,Doors ,drywall repairs, plumbing ,electric,etc ,pretty much everything that has to do with interior and exterior remodeling including Room Additions and New Construction.

As far as the colors and design we would like to keep our company colors.
The attachment I sent with the form that I filled in the Tumbix man it's Representing us us as a company as what we do .
Those are the colors that we would like to keep on the flyer so people could recognize us.

Target Market(s)

We would like to target people ho are doing remodeling like kitchen and bathrooms ,basement then people who needs repair and service calls throughout their homes.

Industry/Entity Type

Construction

```html
<!DOCTYPE html>
<html lang="en">
<head>
<meta charset="utf-8">
<title>Tumbix Remodeling Postcard</title>
<link rel="stylesheet" href="https://fonts.googleapis.com/css2?family=Roboto+Slab:wght@400;500;700;800&family=Roboto+Condensed:wght@700&family=Arimo&display=swap">
<style>
  :root {
    --backdrop: #d2a865;
    --brand-blue: #2859a8;
    --brand-yellow: #f7b928;
    --card-white: #ffffff;
    --logo-grey: #c9c9c9;
    --stamp-grey: #8a8a8a;
    --figure-blue: #3a66b8;
    --figure-yellow: #f2c537;
  }
  * { box-sizing: border-box; margin: 0; padding: 0; }
  html, body { width: 798px; height: 1200px; overflow: hidden; }
  body { position: relative; background: var(--backdrop); font-family: "Roboto Slab", serif; }

  .postcard { position: absolute; left: 50px; width: 698px; height: 538px; background: var(--card-white); overflow: hidden; }
  .postcard--front { top: 50px; }
  .postcard--back { top: 612px; }

  /* Front */
  .front-panel { position: absolute; left: 0; top: 0; width: 380px; height: 538px; background: var(--brand-blue); }
  .front-divider { position: absolute; left: 380px; top: 0; width: 4px; height: 538px; background: var(--brand-yellow); }
  .headline { position: absolute; left: 0; top: 22px; width: 294px; text-align: center; color: var(--brand-yellow);
    font-weight: 500; font-size: 27px; line-height: 40px; white-space: nowrap; }
  .intro { position: absolute; left: 0; top: 106px; width: 294px; text-align: center; color: var(--brand-yellow);
    font-weight: 500; font-size: 19.5px; line-height: 34px; white-space: nowrap; }
  .services-tag { position: absolute; left: 0; top: 259px; width: 210px; height: 27px; }
  .services-tag svg { position: absolute; left: 0; top: 0; }
  .services-tag span { position: absolute; left: 26px; top: 3px; font-weight: 700; font-size: 16px; color: var(--brand-blue); white-space: nowrap; }
  .service-list { position: absolute; top: 296px; list-style: none; color: var(--card-white); font-size: 15px; line-height: 29px; white-space: nowrap; }
  .service-list--first { left: 26px; }
  .service-list--second { left: 212px; }
  .service-list li { display: flex; align-items: center; gap: 13px; }
  .service-list svg { width: 14px; height: 14px; flex: none; }
  .call-band { position: absolute; left: 0; top: 465px; width: 380px; height: 45px; background: var(--brand-yellow);
    color: var(--brand-blue); font-weight: 800; font-size: 21px; line-height: 45px; padding-left: 30px; white-space: nowrap; }
  .logo-name { position: absolute; left: 462px; top: 22px; font-family: "Roboto Condensed", sans-serif; font-weight: 700;
    font-size: 44px; color: var(--logo-grey); letter-spacing: 0.5px; }
  .mascot { position: absolute; background: linear-gradient(170deg, var(--figure-yellow) 0%, var(--figure-blue) 55%, var(--figure-yellow) 100%);
    border-radius: 30px; }
  .mascot--front { left: 398px; top: 100px; width: 286px; height: 424px; }

  /* Back */
  .back-band { position: absolute; left: 0; top: 0; width: 521px; height: 160px; background: var(--brand-blue); text-align: center; }
  .back-kicker { margin-top: 14px; font-weight: 700; font-size: 21px; color: var(--brand-yellow); line-height: 28px; }
  .back-rooms { color: var(--card-white); font-size: 21px; line-height: 30px; white-space: nowrap; }
  .back-call { margin-top: 6px; font-weight: 800; font-size: 24px; color: var(--brand-yellow); line-height: 30px; white-space: nowrap; }
  .stamp-box { position: absolute; left: 560px; top: 40px; width: 94px; height: 104px; border: 1px solid var(--stamp-grey);
    display: flex; align-items: center; justify-content: center; text-align: center;
    font-family: "Arimo", sans-serif; font-size: 15.5px; line-height: 20px; color: var(--stamp-grey); }
  .mascot--back { left: 40px; top: 173px; width: 260px; height: 270px; border-radius: 26px; }
</style>
</head>
<body>

<section class="postcard postcard--front">
  <div class="front-panel">
    <h1 class="headline">EVERYTHING<br>UNDER ONE ROOF</h1>
    <p class="intro">Interior and Exterior<br>Remodeling including<br>Room Additions and<br>New Construction.</p>

    <div class="services-tag">
      <svg width="210" height="27" viewBox="0 0 210 27"><polygon points="0,0 196,0 210,27 0,27" fill="#f7b928"/></svg>
      <span>WE ARE DOING:</span>
    </div>

    <ul class="service-list service-list--first">
      <li><svg viewBox="0 0 14 14"><rect x="0.75" y="0.75" width="12.5" height="12.5" fill="none" stroke="#f7b928" stroke-width="1.5"/><path d="M3 7.2 L6 10 L11 3.8" fill="none" stroke="#f7b928" stroke-width="1.8"/></svg>Hardwood Floors</li>
      <li><svg viewBox="0 0 14 14"><rect x="0.75" y="0.75" width="12.5" height="12.5" fill="none" stroke="#f7b928" stroke-width="1.5"/><path d="M3 7.2 L6 10 L11 3.8" fill="none" stroke="#f7b928" stroke-width="1.8"/></svg>Ceramic Tile</li>
      <li><svg viewBox="0 0 14 14"><rect x="0.75" y="0.75" width="12.5" height="12.5" fill="none" stroke="#f7b928" stroke-width="1.5"/><path d="M3 7.2 L6 10 L11 3.8" fill="none" stroke="#f7b928" stroke-width="1.8"/></svg>Baseboards</li>
      <li><svg viewBox="0 0 14 14"><rect x="0.75" y="0.75" width="12.5" height="12.5" fill="none" stroke="#f7b928" stroke-width="1.5"/><path d="M3 7.2 L6 10 L11 3.8" fill="none" stroke="#f7b928" stroke-width="1.8"/></svg>Drywall Repairs</li>
      <li><svg viewBox="0 0 14 14"><rect x="0.75" y="0.75" width="12.5" height="12.5" fill="none" stroke="#f7b928" stroke-width="1.5"/><path d="M3 7.2 L6 10 L11 3.8" fill="none" stroke="#f7b928" stroke-width="1.8"/></svg>Electric etc.</li>
    </ul>
    <ul class="service-list service-list--second">
      <li><svg viewBox="0 0 14 14"><rect x="0.75" y="0.75" width="12.5" height="12.5" fill="none" stroke="#f7b928" stroke-width="1.5"/><path d="M3 7.2 L6 10 L11 3.8" fill="none" stroke="#f7b928" stroke-width="1.8"/></svg>Painting</li>
      <li><svg viewBox="0 0 14 14"><rect x="0.75" y="0.75" width="12.5" height="12.5" fill="none" stroke="#f7b928" stroke-width="1.5"/><path d="M3 7.2 L6 10 L11 3.8" fill="none" stroke="#f7b928" stroke-width="1.8"/></svg>Casings</li>
      <li><svg viewBox="0 0 14 14"><rect x="0.75" y="0.75" width="12.5" height="12.5" fill="none" stroke="#f7b928" stroke-width="1.5"/><path d="M3 7.2 L6 10 L11 3.8" fill="none" stroke="#f7b928" stroke-width="1.8"/></svg>Doors</li>
      <li><svg viewBox="0 0 14 14"><rect x="0.75" y="0.75" width="12.5" height="12.5" fill="none" stroke="#f7b928" stroke-width="1.5"/><path d="M3 7.2 L6 10 L11 3.8" fill="none" stroke="#f7b928" stroke-width="1.8"/></svg>Plumbing</li>
    </ul>

    <div class="call-band">Call Us Today: 0044556677</div>
  </div>
  <div class="front-divider"></div>

  <div class="logo-name">TUMBIX</div>
  <div class="mascot mascot--front" role="img" aria-label="Illustration of the Tumbix builder mascot in a yellow hard hat and blue overalls with a tool belt, holding a small house and a set of keys"></div>
</section>

<section class="postcard postcard--back">
  <div class="back-band">
    <p class="back-kicker">Remodel YOUR</p>
    <p class="back-rooms">Home | Bathrooms | Kitchen | Basement<br>Interior | Exterior Work.</p>
    <p class="back-call">Call Us Today: 0044556677</p>
  </div>
  <div class="stamp-box">Place<br>Stamp<br>Here</div>
  <div class="mascot mascot--back" role="img" aria-label="Smaller illustration of the Tumbix builder mascot holding a house and keys"></div>
</section>

</body>
</html>
```